Women's Health Company needs business card

We need a business card for a USA based women's health care company. We use digital technology to enhance therapy prescribed by clinicians for their patients

```html
<!DOCTYPE html>
<html lang="en">
<head>
<meta charset="utf-8">
<title>Lorvina Care – Business Card</title>
<link rel="stylesheet" href="https://fonts.googleapis.com/css2?family=Arimo:wght@400;700&display=swap">
<style>
  :root {
    --teal: #72bdb9;
    --purple: #8a4f9e;
    --white: #ffffff;
    --backdrop: #b5b3ae;
    --card-w: 520px;
    --card-h: 297px;
  }
  * { margin: 0; padding: 0; box-sizing: border-box; }
  html, body {
    width: 1200px;
    height: 857px;
    overflow: hidden;
    background: var(--backdrop);
    font-family: "Arimo", Arial, sans-serif;
  }
  .stage {
    width: 1200px;
    height: 857px;
    display: flex;
    align-items: center;
    justify-content: center;
    gap: 60px;
  }
  .card {
    position: relative;
    width: var(--card-w);
    height: var(--card-h);
    overflow: hidden;
    border-bottom: 3px solid var(--purple);
    box-shadow: 0 8px 18px rgba(0,0,0,0.25);
  }
  .card--front { background: var(--white); }
  .card--back { background: var(--teal); }
  .card__wave {
    position: absolute;
    inset: 0;
    width: 100%;
    height: 100%;
  }
  .brand {
    position: absolute;
    display: flex;
    align-items: center;
    gap: 6px;
    font-weight: 400;
    letter-spacing: 0.5px;
    white-space: nowrap;
  }
  .brand__dot {
    border-radius: 50%;
    background: var(--purple);
    flex: none;
  }
  .card--front .brand {
    left: 28px;
    top: 128px;
    font-size: 28px;
    color: var(--teal);
  }
  .card--front .brand__dot { width: 8px; height: 8px; }
  .card--back .brand {
    left: 50%;
    top: 50%;
    transform: translate(-50%, -50%);
    font-size: 54px;
    color: var(--white);
  }
  .card--back .brand__dot { width: 14px; height: 14px; }
  .contact {
    position: absolute;
    left: 300px;
    top: 92px;
    color: var(--white);
  }
  .contact__name {
    font-size: 17px;
    font-weight: 700;
    letter-spacing: 0.4px;
    text-transform: uppercase;
  }
  .contact__role {
    font-size: 12px;
    margin-top: 2px;
  }
  .contact__list {
    list-style: none;
    margin-top: 22px;
    font-size: 11.5px;
  }
  .contact__list li {
    display: flex;
    align-items: center;
    gap: 8px;
    margin-bottom: 5px;
  }
  .contact__icon { width: 10px; height: 10px; flex: none; }
</style>
</head>
<body>
<main class="stage">
  <section class="card card--front" aria-label="Card front">
    <svg class="card__wave" viewBox="0 0 520 297" preserveAspectRatio="none" aria-hidden="true">
      <path d="M520 0 L300 0 C232 40 240 120 228 180 C218 240 228 270 240 297 L520 297 Z" fill="var(--purple)"/>
      <path d="M520 0 L310 0 C244 42 252 122 240 182 C230 240 240 270 252 297 L520 297 Z" fill="var(--teal)"/>
    </svg>
    <div class="brand"><span class="brand__dot"></span>Lorvina Care</div>
    <div class="contact">
      <p class="contact__name">Daniel Porter</p>
      <p class="contact__role">Operational Manager</p>
      <ul class="contact__list">
        <li>
          <svg class="contact__icon" viewBox="0 0 10 10" aria-hidden="true"><path d="M2 1 L4 1 L4.6 3 L3.4 3.8 Q4.4 5.8 6.2 6.6 L7 5.4 L9 6 L9 8 Q5 9 1 2 Z" fill="var(--white)"/></svg>
          +1.555.210.4836
        </li>
        <li>
          <svg class="contact__icon" viewBox="0 0 10 10" aria-hidden="true"><rect x="0.5" y="2" width="9" height="6" fill="var(--white)"/><path d="M0.5 2 L5 5.5 L9.5 2" stroke="var(--teal)" stroke-width="0.8" fill="none"/></svg>
          hello@lorvinacare.com
        </li>
        <li>
          <svg class="contact__icon" viewBox="0 0 10 10" aria-hidden="true"><circle cx="5" cy="5" r="4.3" fill="none" stroke="var(--white)" stroke-width="1"/><path d="M0.7 5 H9.3 M5 0.7 Q2.5 5 5 9.3 M5 0.7 Q7.5 5 5 9.3" stroke="var(--white)" stroke-width="0.8" fill="none"/></svg>
          www.lorvinacare.com
        </li>
      </ul>
    </div>
  </section>

  <section class="card card--back" aria-label="Card back">
    <div class="brand"><span class="brand__dot"></span>Lorvina Care</div>
  </section>
</main>
</body>
</html>
```